Website Design For Physical Therapy/Sports Massage Clinic

Hi! I am looking for a sleek, fun and functional new wordpress website for my physical therapy/sports massage clinic. My current site is www.quorvanmotion.com. As you can see it's very basic and well... boring. :) In addition to a fun new look, I would also love this to be mobile friendly.

In terms of add on services/widgets I would like to use Zindleby Booking + Veltro Consent so that people can schedule and fill out paperwork remotely. Both seem like easy add ons to any site, but just in case here are the sites for both to ensure compatibility with the new design.

https://secure.zindlebybooking.com/
https://www.veltroconsent.com/

Thanks for reading and I'm excited to get started. I would love to see designs that are modern, athlete minded and fun as those are my clients. Attached you will find two logos (one white and one blue).

Target Market(s)

Athletes and weekend warriors

Industry/Entity Type

Physical Therapy

Number of Pages Required

1 page

Font styles to use
Sans Serif

Requirements
Must have
• 1) A fun home page that is modern and easy to navigate and 2) a website that is compatible with Zindleby booking + veltro consent so that my patients can schedule and fill out their paperwork without me.

```html
<!DOCTYPE html>
<html lang="en">
<head>
<meta charset="utf-8">
<title>Quorvan Motion Therapy</title>
<link href="https://fonts.googleapis.com/css2?family=Open+Sans:wght@400;600;700;800&display=swap" rel="stylesheet">
<style>
:root{
  --orange:#f47b20;
  --blue:#1c5693;
  --blue-dark:#17477b;
  --ink:#2b2b2b;
  --text:#555;
  --nav:#333333;
  --light:#f3f3f3;
  --footer:#2f2f2f;
  --footer-bar:#232323;
  --white:#fff;
}
*{box-sizing:border-box;margin:0;padding:0}
html,body{width:1200px;height:3782px;overflow:hidden}
body{font-family:"Open Sans",Arial,sans-serif;color:var(--text);background:var(--white)}
.page{position:relative;width:1200px;height:3782px;overflow:hidden}
.abs{position:absolute}
.section-title{position:absolute;left:0;width:1200px;text-align:center;font-size:27px;font-weight:700;text-transform:uppercase;color:var(--blue);letter-spacing:.5px}
.section-title span{color:var(--orange)}
.section-title::before{content:"";position:absolute;left:50%;transform:translateX(-50%);top:-14px;width:270px;height:2px;background:#bbb}
.section-title::after{content:"";position:absolute;left:50%;transform:translateX(-50%);bottom:-12px;width:270px;height:2px;background:#bbb}
.chev{font-weight:800;letter-spacing:-3px;margin-right:8px}
.btn{position:absolute;display:flex;align-items:center;justify-content:center;font-size:14px;font-weight:600;text-transform:uppercase;color:var(--white);letter-spacing:.3px}
.btn-blue{background:var(--blue)}
.btn-orange{background:var(--orange)}
/* header */
.site-header{position:absolute;left:0;top:0;width:1200px;height:96px;background:var(--white)}
.brand{position:absolute;left:101px;top:30px;display:flex;align-items:center;gap:12px;font-size:26px;font-weight:700;color:var(--blue)}
.brand-mark{width:34px;height:34px;background:var(--orange);border-radius:50%}
.phone{position:absolute;left:618px;top:30px;display:flex;align-items:center;gap:10px;font-size:22px;color:var(--ink)}
.phone-icon{width:30px;height:30px;border-radius:50%;background:var(--orange);display:flex;align-items:center;justify-content:center}
.header-cta{position:absolute;left:832px;top:26px;width:270px;height:38px;border-top:2px solid var(--blue);border-bottom:2px solid var(--blue);display:flex;align-items:center;justify-content:center;gap:8px;font-size:15px;font-weight:600;color:var(--blue);text-transform:uppercase}
.main-nav{position:absolute;left:353px;top:96px;width:847px;height:43px;background:var(--nav)}
.main-nav a{position:absolute;top:0;height:43px;line-height:43px;color:var(--white);font-size:16px;text-decoration:none}
.main-nav a.active{background:var(--orange);padding:0 30px 0 18px}
/* hero */
.hero{position:absolute;left:0;top:139px;width:1200px;height:511px;background:linear-gradient(120deg,#3b4a2a 0%,#6b7a3e 30%,#c9b47a 55%,#f4e0a8 65%,#8a8366 80%,#4a4c3c 100%)}
.hero-caption{position:absolute;left:101px;top:264px;width:570px;height:114px;background:rgba(20,20,20,.55);padding:12px 16px;color:var(--white);font-size:33px;font-weight:600;line-height:47px;text-transform:uppercase}
.hero-dots{position:absolute;left:567px;top:462px;display:flex;gap:6px}
.hero-dots i{width:11px;height:11px;border-radius:50%;background:rgba(255,255,255,.7);display:block}
.hero-dots i.on{background:var(--orange)}
/* about */
.about{position:absolute;left:0;top:650px;width:1200px;height:472px;background:var(--white)}
.about-title{position:absolute;left:101px;top:52px;width:326px;padding:6px 0;border-top:2px solid #bbb;border-bottom:2px solid #bbb;font-size:26px;font-weight:700;color:var(--blue);text-transform:uppercase}
.about-title span{color:var(--orange)}
.about-copy{position:absolute;left:101px;top:118px;width:655px;font-size:15px;line-height:24px}
.about-copy p{margin-bottom:14px}
.about .btn{left:101px;top:362px;width:165px;height:38px}
.appt{position:absolute;left:784px;top:51px;width:317px;height:370px;background:var(--white);border:1px solid #ddd;box-shadow:0 2px 8px rgba(0,0,0,.1)}
.appt-head{height:58px;background:var(--blue);color:var(--white);font-size:17px;font-weight:600;text-transform:uppercase;display:flex;align-items:center;justify-content:center;position:relative}
.appt-head::after{content:"";position:absolute;bottom:-12px;left:50%;margin-left:-12px;border-left:12px solid transparent;border-right:12px solid transparent;border-top:12px solid var(--blue)}
.field{position:absolute;left:18px;width:280px;height:40px;border:1px solid #ccc;font-size:13px;color:#666;padding:10px 12px}
.appt .btn{left:18px;top:322px;width:280px;height:38px;font-size:14px}
/* services */
.services{position:absolute;left:0;top:1122px;width:1200px;height:567px;background:var(--light)}
.services-band{position:absolute;left:0;top:378px;width:1200px;height:189px;background:var(--blue)}
.service{position:absolute;top:154px;width:318px}
.service-photo{height:280px;border:4px solid var(--orange)}
.service-badge{position:absolute;left:126px;top:236px;width:64px;height:64px;border-radius:50%;background:var(--orange);display:flex;align-items:center;justify-content:center}
.service-name{margin-top:30px;color:var(--white);font-size:18px;font-weight:600;text-transform:uppercase;line-height:24px}
/* why */
.why{position:absolute;left:0;top:1689px;width:1200px;height:593px;background:#fbfbfb}
.feature{position:absolute;width:260px;text-align:center}
.feature h3{font-size:18px;font-weight:600;color:var(--ink)}
.feature p{font-size:14px;line-height:20px;margin-top:6px}
.feature .dot{display:block;margin:10px auto 0;width:24px;height:24px;border-radius:50%;background:var(--orange)}
.feature.down .dot{background:var(--blue)}
/* testimonials */
.testimonials{position:absolute;left:0;top:2282px;width:1200px;height:360px;background:linear-gradient(90deg,#2a2424 0%,#5a3a2e 40%,#7a4a36 60%,#3a2d29 100%)}
.testimonials::after{content:"";position:absolute;inset:0;background:rgba(0,0,0,.45)}
.testimonials > *{z-index:1}
.testimonials .section-title{top:40px;color:var(--white)}
.testimonials .section-title::before,.testimonials .section-title::after{background:rgba(255,255,255,.5)}
.avatar{position:absolute;width:100px;height:100px;border-radius:50%;border:4px solid var(--white);background:linear-gradient(#c9a58a,#8a6a55)}
.quote{position:absolute;width:330px;height:131px;border:1px solid rgba(255,255,255,.5);background:rgba(0,0,0,.25);padding:12px 16px 0 40px;color:#eee;font-size:13px;line-height:19px}
.quote::before{content:"\201C";position:absolute;left:12px;top:2px;font-size:40px;color:var(--orange);font-weight:700}
.quote small{display:block;margin-top:8px;font-size:11px;color:#ccc}
.cite{position:absolute;font-size:14px;font-weight:600;color:var(--white)}
.cite span{color:var(--orange);font-weight:400}
.arrow-side{position:absolute;width:24px;height:40px}
/* blog */
.blog{position:absolute;left:0;top:2642px;width:1200px;height:572px;background:#f6f6f6}
.post{position:absolute;top:149px;width:318px;height:368px;background:var(--white);box-shadow:0 1px 4px rgba(0,0,0,.08)}
.post-photo{height:179px}
.post h4{margin:22px 0 0 17px;font-size:17px;font-weight:600;color:var(--ink)}
.post .meta{margin:4px 0 0 17px;font-size:11px;color:#888}
.post .excerpt{margin:6px 17px 0;font-size:13px;line-height:18px}
.post .btn{left:17px;top:310px;width:156px;height:35px;font-size:13px}
/* newsletter */
.newsletter{position:absolute;left:0;top:3214px;width:1200px;height:240px;background:linear-gradient(90deg,#1c5693,#2c6aa8 50%,#1c5693);border-bottom:5px solid var(--orange)}
.newsletter .section-title{top:62px;color:var(--white)}
.newsletter .section-title::before,.newsletter .section-title::after{background:rgba(255,255,255,.5)}
.nl-input{position:absolute;left:270px;top:152px;width:486px;height:34px;background:var(--white);font-size:13px;color:#777;padding:8px 12px}
.newsletter .btn{left:784px;top:152px;width:144px;height:34px}
/* footer */
.site-footer{position:absolute;left:0;top:3454px;width:1200px;height:290px;background:var(--footer);color:#ccc;font-size:13px}
.fcol{position:absolute;top:52px}
.fcol h5{font-size:15px;font-weight:700;color:var(--white);text-transform:uppercase;margin-bottom:14px}
.fcol ul{list-style:none}
.fcol li{line-height:25px}
.fcol li::before{content:"\00BB";color:var(--orange);margin-right:6px}
.fcol li.on{color:var(--orange)}
.fcol p{line-height:20px}
.fcontact{display:flex;align-items:center;gap:8px;margin-top:10px}
.fcontact i{width:14px;height:14px;border-radius:50%;background:#888;display:block}
.map{position:absolute;left:540px;top:88px;width:287px;height:169px;background:linear-gradient(135deg,#e8e6df,#d7dccf);border:3px solid var(--white)}
.flogo{position:absolute;left:892px;top:210px;display:flex;align-items:center;gap:10px;font-size:18px;font-weight:700;color:#ddd}
.flogo i{width:26px;height:26px;background:var(--orange);display:block}
.footer-bar{position:absolute;left:0;top:3744px;width:1200px;height:38px;background:var(--footer-bar);color:#aaa;font-size:12px}
.footer-bar p{position:absolute;left:101px;top:11px}
.social{position:absolute;right:101px;top:8px;display:flex;gap:8px}
.social i{width:22px;height:22px;border-radius:50%;border:1px solid #aaa;display:block}
</style>
</head>
<body>
<div class="page">

<header class="site-header">
  <div class="brand"><span class="brand-mark"></span>Quorvan Motion Therapy</div>
  <div class="phone"><span class="phone-icon"><svg width="16" height="16" viewBox="0 0 24 24"><path d="M6.6 10.8a15 15 0 0 0 6.6 6.6l2.2-2.2a1 1 0 0 1 1-.25 11.4 11.4 0 0 0 3.6.57 1 1 0 0 1 1 1V20a1 1 0 0 1-1 1A17 17 0 0 1 3 4a1 1 0 0 1 1-1h3.5a1 1 0 0 1 1 1c0 1.25.2 2.45.57 3.57a1 1 0 0 1-.25 1z" fill="#fff"/></svg></span>(512) 555-0148</div>
  <div class="header-cta"><svg width="16" height="16" viewBox="0 0 24 24"><rect x="3" y="5" width="18" height="16" fill="none" stroke="#1c5693" stroke-width="2"/><line x1="3" y1="10" x2="21" y2="10" stroke="#1c5693" stroke-width="2"/></svg>Schedule an Appointment</div>
</header>

<nav class="main-nav">
  <a class="active" style="left:0">Home <span class="chev">»</span></a>
  <a style="left:116px">About</a>
  <a style="left:214px">Services</a>
  <a style="left:328px">New Patients</a>
  <a style="left:479px">Pricing</a>
  <a style="left:580px">Blog</a>
  <a style="left:668px">Contact</a>
</nav>

<section class="hero" role="img" aria-label="Runner jogging along a sunlit tree-lined road at sunset">
  <div class="hero-caption">Pain and injury keeping you from your active lifestyle?</div>
  <svg class="abs" style="left:655px;top:264px" width="60" height="114" viewBox="0 0 60 114"><path d="M0 0 L38 57 L0 114 H18 L56 57 L18 0Z" fill="#f47b20"/></svg>
  <div class="hero-dots"><i class="on"></i><i></i><i></i><i></i></div>
</section>

<section class="about">
  <h2 class="about-title"><span class="chev" style="color:var(--blue)">»</span>About <span>Sports Therapy</span></h2>
  <div class="about-copy">
    <p>Quorvan Motion Therapy is not your average Physical Therapy clinic. Here you will never find a room full of patients working out simultaneously. Nor will you experience a visit that consists solely of modalities and exercise. Instead, you will find effective, 1-on-1 care that delivers the skilled hands-on/manual therapy that you need.</p>
    <p>Upon starting treatment, you will first undergo a thorough evaluation to determine not only your diagnosis, but also the causes behind it. What breaks and why are rarely the same and a comprehensive, full body approach will be used to identify contributing factors such as mobility, strength, posture, and bio-mechanics/sports technique.</p>
  </div>
  <a class="btn btn-blue">Learn More <span class="chev" style="margin:0 0 0 8px">»</span></a>

  <form class="appt">
    <div class="appt-head">Schedule an Appointment</div>
    <div class="field" style="top:98px">Name</div>
    <div class="field" style="top:144px">Email</div>
    <div class="field" style="top:190px">Phone</div>
    <div class="field" style="top:236px;height:62px">Brief description of your problem</div>
    <div class="btn btn-orange">Schedule an Appointment <span class="chev" style="margin:0 0 0 8px">»</span></div>
  </form>
</section>

<section class="services">
  <h2 class="section-title" style="top:64px"><span class="chev" style="color:var(--blue)">»</span>Our <span>Services</span></h2>
  <div class="services-band"></div>
  <div class="service" style="left:101px">
    <div class="service-photo" role="img" aria-label="Therapist treating a patient's shoulder" style="background:linear-gradient(135deg,#d9cfc4,#a89080)"></div>
    <div class="service-badge"><svg width="30" height="30" viewBox="0 0 24 24"><circle cx="12" cy="6" r="3" fill="#fff"/><rect x="4" y="13" width="16" height="4" fill="#fff"/></svg></div>
    <div class="service-name">Physical Therapy <span class="chev">»</span></div>
  </div>
  <div class="service" style="left:441px">
    <div class="service-photo" role="img" aria-label="Coach guiding an athlete through strength training" style="background:linear-gradient(135deg,#c7ccd2,#7b8a99)"></div>
    <div class="service-badge"><svg width="30" height="30" viewBox="0 0 24 24"><rect x="2" y="10" width="20" height="3" fill="#fff"/><rect x="4" y="6" width="3" height="11" fill="#fff"/><rect x="17" y="6" width="3" height="11" fill="#fff"/></svg></div>
    <div class="service-name">Sport Specific Analysis<br>&amp; Training <span class="chev">»</span></div>
  </div>
  <div class="service" style="left:781px">
    <div class="service-photo" role="img" aria-label="Massage therapist working on a client's back" style="background:linear-gradient(135deg,#e3cbb6,#a8806a)"></div>
    <div class="service-badge"><svg width="30" height="30" viewBox="0 0 24 24"><circle cx="7" cy="7" r="2.5" fill="#fff"/><circle cx="17" cy="7" r="2.5" fill="#fff"/><rect x="5" y="11" width="4" height="9" fill="#fff"/><rect x="15" y="11" width="4" height="9" fill="#fff"/></svg></div>
    <div class="service-name">Wellness &amp; Maintenance<br>Care <span class="chev">»</span></div>
  </div>
</section>

<section class="why">
  <h2 class="section-title" style="top:64px"><span class="chev" style="color:var(--blue)">»</span>Why <span>Choose Us?</span></h2>

  <div class="feature" style="left:69px;top:157px"><h3>Quality Hands On Time</h3><p>Duis autem vel eum iriure do<br>in hendrerit in vulputate.</p><i class="dot"></i></div>
  <div class="feature" style="left:392px;top:157px"><h3>Education</h3><p>Duis autem vel eum iriure do<br>in hendrerit in vulputate.</p><i class="dot"></i></div>
  <div class="feature" style="left:710px;top:157px"><h3>Comfortable Clinic</h3><p>Duis autem vel eum iriure do<br>in hendrerit in vulputate.</p><i class="dot"></i></div>

  <svg class="abs" style="left:0;top:198px" width="1200" height="300" viewBox="0 0 1200 300" aria-hidden="true">
    <line x1="101" y1="150" x2="103" y2="150" stroke="#f47b20" stroke-width="30"/>
    <path d="M103 150 A96 96 0 0 0 295 150" fill="none" stroke="#f47b20" stroke-width="30"/>
    <path d="M264 150 A96 96 0 0 1 456 150" fill="none" stroke="#1c5693" stroke-width="30"/>
    <path d="M426 150 A96 96 0 0 0 618 150" fill="none" stroke="#f47b20" stroke-width="30"/>
    <path d="M585 150 A96 96 0 0 1 777 150" fill="none" stroke="#1c5693" stroke-width="30"/>
    <path d="M744 150 A96 96 0 0 0 936 150" fill="none" stroke="#f47b20" stroke-width="30"/>
    <path d="M905 150 A96 96 0 0 1 1097 150" fill="none" stroke="#1c5693" stroke-width="30"/>
    <g fill="#fff" stroke="#e2e2e2" stroke-width="2">
      <circle cx="199" cy="150" r="63"/><circle cx="360" cy="150" r="63"/><circle cx="522" cy="150" r="63"/>
      <circle cx="681" cy="150" r="63"/><circle cx="840" cy="150" r="63"/><circle cx="1001" cy="150" r="63"/>
    </g>
    <g fill="none" stroke="#333" stroke-width="4">
      <circle cx="199" cy="152" r="20"/><path d="M199 140 V152 L208 158"/><path d="M193 126 H205"/>
      <circle cx="360" cy="132" r="6" fill="#333"/><path d="M344 160 H376 M350 146 L370 146"/>
      <rect x="508" y="128" width="28" height="22"/><circle cx="512" cy="164" r="5" fill="#333"/><circle cx="532" cy="164" r="5" fill="#333"/>
      <circle cx="677" cy="146" r="12"/><path d="M686 155 L697 166"/>
      <path d="M820 150 L840 132 L860 150 V170 H820Z"/><path d="M840 148 V164 M832 156 H848"/>
      <circle cx="986" cy="140" r="6" fill="#333"/><circle cx="1016" cy="140" r="6" fill="#333"/><circle cx="1001" cy="136" r="7" fill="#333"/><path d="M980 166 Q1001 148 1022 166"/>
    </g>
  </svg>

  <div class="feature down" style="left:230px;top:442px"><h3>Effective Treatments</h3><p>Duis autem vel eum iriure do<br>in hendrerit in vulputate.</p><i class="dot"></i></div>
  <div class="feature down" style="left:551px;top:442px"><h3>Experience Staff</h3><p>Duis autem vel eum iriure do<br>in hendrerit in vulputate.</p><i class="dot"></i></div>
  <div class="feature down" style="left:871px;top:442px"><h3>Practitioners Network</h3><p>Duis autem vel eum iriure do<br>in hendrerit in vulputate.</p><i class="dot"></i></div>
</section>

<section class="testimonials" role="img" aria-label="Athlete stretching on an exercise ball">
  <h2 class="section-title"><span class="chev" style="color:var(--white)">»</span>Clients <span>Testimonials</span></h2>
  <svg class="arrow-side" style="left:50px;top:156px" viewBox="0 0 24 40"><path d="M20 2 L4 20 L20 38" fill="none" stroke="#ccc" stroke-width="3"/></svg>
  <svg class="arrow-side" style="right:50px;top:156px" viewBox="0 0 24 40"><path d="M4 2 L20 20 L4 38" fill="none" stroke="#ccc" stroke-width="3"/></svg>
  <div class="avatar" style="left:101px;top:164px" role="img" aria-label="Client portrait"></div>
  <div class="quote" style="left:240px;top:146px">Ut wisi enim ad minim veniam, quisl mor nostrud exerci tation ullamcorper suscipit no lobortis nisl nisl ut aliquip.<small>4:04PM – 31 MAY, 2016</small></div>
  <div class="cite" style="left:270px;top:293px">Mr. Tarin Oakes <span>@toakes</span></div>
  <div class="avatar" style="left:631px;top:164px" role="img" aria-label="Client portrait"></div>
  <div class="quote" style="left:771px;top:146px">Ut wisi enim ad minim veniam, quisl mor nostrud exerci tation ullamcorper suscipit no lobortis nisl nisl ut aliquip.<small>4:04PM – 31 MAY, 2016</small></div>
  <div class="cite" style="left:801px;top:293px">Mrs. Jenie Marlowe <span>@jmarlowe</span></div>
</section>

<section class="blog">
  <h2 class="section-title" style="top:64px"><span class="chev" style="color:var(--blue)">»</span>Latest <span>Blog Post</span></h2>
  <svg class="arrow-side" style="left:50px;top:310px" viewBox="0 0 24 40"><path d="M20 2 L4 20 L20 38" fill="none" stroke="#bbb" stroke-width="3"/></svg>
  <svg class="arrow-side" style="right:50px;top:310px" viewBox="0 0 24 40"><path d="M4 2 L20 20 L4 38" fill="none" stroke="#bbb" stroke-width="3"/></svg>
  <article class="post" style="left:101px">
    <div class="post-photo" role="img" aria-label="Therapist guiding a patient with a resistance band" style="background:linear-gradient(135deg,#e6dccf,#b7a898)"></div>
    <h4>Consectetuer Adipiscing</h4><div class="meta">By Tarin Oakes &nbsp; May 31, 2016</div>
    <p class="excerpt">Ut wisi enim ad minim veniam, quismi nostr exerci tation ullamcorper consequat.</p>
    <a class="btn btn-blue">Read More <span class="chev" style="margin:0 0 0 8px">»</span></a>
  </article>
  <article class="post" style="left:441px">
    <div class="post-photo" role="img" aria-label="Therapist stretching a patient on an exercise mat" style="background:linear-gradient(135deg,#d6dde2,#9ba8a8)"></div>
    <h4>Consectetuer Adipiscing</h4><div class="meta">By Tarin Oakes &nbsp; May 31, 2016</div>
    <p class="excerpt">Ut wisi enim ad minim veniam, quismi nostr exerci tation ullamcorper consequat.</p>
    <a class="btn btn-blue">Read More <span class="chev" style="margin:0 0 0 8px">»</span></a>
  </article>
  <article class="post" style="left:781px">
    <div class="post-photo" role="img" aria-label="Therapist treating a patient's leg" style="background:linear-gradient(135deg,#dcd3cf,#7f8a97)"></div>
    <h4>Consectetuer Adipiscing</h4><div class="meta">By Tarin Oakes &nbsp; May 31, 2016</div>
    <p class="excerpt">Ut wisi enim ad minim veniam, quismi nostr exerci tation ullamcorper consequat.</p>
    <a class="btn btn-blue">Read More <span class="chev" style="margin:0 0 0 8px">»</span></a>
  </article>
</section>

<section class="newsletter">
  <h2 class="section-title"><span class="chev" style="color:var(--white)">»</span>Newsletter <span>Signup</span></h2>
  <div class="nl-input">Enter your email here</div>
  <a class="btn btn-orange">Signup <span class="chev" style="margin:0 0 0 8px">»</span></a>
</section>

<footer class="site-footer">
  <div class="fcol" style="left:101px">
    <h5>Quick Links</h5>
    <ul><li class="on">Home</li><li>About</li><li>Services</li><li>New Patients</li><li>Pricing</li><li>Blog</li><li>Contact</li></ul>
  </div>
  <div class="fcol" style="left:272px">
    <h5>Contact Information</h5>
    <p style="color:#fff">Quorvan Motion Therapy</p>
    <p>2180 Larkmoor Rd, Ste 310<br>Brennick, TX 78000</p>
    <div class="fcontact"><i></i>555-201-0172</div>
    <div class="fcontact"><i></i>555-201-0193</div>
    <div class="fcontact"><i></i>info@quorvanmotion.com</div>
  </div>
  <div class="fcol" style="left:540px"><h5>Location Map</h5></div>
  <div class="map" role="img" aria-label="Street map showing the clinic location">
    <svg class="abs" style="left:60px;top:90px" width="22" height="30" viewBox="0 0 22 30"><path d="M11 0a11 11 0 0 1 11 11c0 8-11 19-11 19S0 19 0 11A11 11 0 0 1 11 0z" fill="#d9342b"/><circle cx="11" cy="11" r="4" fill="#fff"/></svg>
  </div>
  <div class="fcol" style="left:892px;width:210px">
    <h5>Opening Hours</h5>
    <p>Open M-F. Please call or use the contact form to schedule your appointment!</p>
  </div>
  <div class="flogo"><i></i>Quorvan Motion</div>
</footer>
<div class="footer-bar">
  <p>© 2016 Quorvan Motion Therapy. All Rights Reserved.</p>
  <div class="social"><i></i><i></i><i></i></div>
</div>

</div>
</body>
</html>
```